New Organic Medical Marijuana Packging Design

New Organic Grower needs a fresh new design for the retail package.
the idea is to incorporate a compostable materials and come up with the resealable pouch/baggy that can hold the medicine and maybe another compartment for the promotional material (like rolling papers).
Company name is Bram's Organic. (bram- Bramwell is the name of our guru grower who also spends a ton of time playing in the dirt).
Medicine will need to be visible (whole or partially )through the side of the pack. an idea attached..

```html
<!DOCTYPE html>
<html lang="en">
<head>
<meta charset="utf-8">
<title>Bram's Organic – Pouch Design</title>
<link href="https://fonts.googleapis.com/css2?family=Montserrat:wght@400;500;600&display=swap" rel="stylesheet">
<style>
  :root {
    --bg-top: #ececec;
    --bg-bottom: #f8f8f8;
    --pouch: #ffffff;
    --pouch-edge: #e4e4e4;
    --seal: #9a9a9a;
    --green: #5cb947;
    --green-light: #7cc96a;
    --ink: #2b2b2b;
    --ink-soft: #555555;
    --blush: #fad3d3;
  }
  * { margin: 0; padding: 0; box-sizing: border-box; }
  html, body { width: 1200px; height: 1000px; overflow: hidden; }
  body {
    background: linear-gradient(180deg, var(--bg-top) 0%, var(--bg-top) 55%, var(--bg-bottom) 100%);
    font-family: "Montserrat", Arial, sans-serif;
    color: var(--ink);
    position: relative;
  }
  .brand-wordmark {
    position: absolute;
    left: 0; width: 1200px;
    top: 160px;
    text-align: center;
    font-weight: 500;
    font-size: 56px;
    letter-spacing: 4px;
    text-transform: uppercase;
    color: var(--ink);
  }
  .brand-wordmark .dot {
    display: inline-block;
    width: 22px; height: 22px;
    border-radius: 50%;
    background: var(--green);
    margin-left: 18px;
    vertical-align: middle;
  }
  .pouch {
    position: absolute;
    top: 368px;
    width: 492px;
    height: 517px;
    background: var(--pouch);
    border-left: 12px solid var(--pouch-edge);
    border-right: 12px solid var(--pouch-edge);
    box-shadow: 0 0 0 1px #e9e9e9;
  }
  .pouch--front { left: 83px; }
  .pouch--back { left: 632px; }
  .pouch__seal {
    position: absolute;
    left: -12px; top: 0;
    width: 14px; height: 32px;
    background: var(--seal);
  }
  .pouch__band {
    position: absolute;
    left: 193px; top: 0;
    width: 84px; height: 187px;
    background: var(--green);
  }
  .pouch__band-stripes {
    position: absolute; left: 0; top: 0; width: 84px; height: 30px;
    background: repeating-linear-gradient(180deg, var(--green-light) 0 2px, var(--green) 2px 5px);
  }
  .pouch__cross { position: absolute; left: 14px; top: 114px; }
  .pouch__warning {
    position: absolute; left: 0; width: 100%; top: 214px;
    text-align: center; font-size: 13px; line-height: 17px;
  }
  .pouch__warning strong { font-weight: 600; display: block; }
  .pouch__product-photo {
    position: absolute;
    left: 85px; top: 268px;
    width: 300px; height: 99px;
    background: var(--blush);
  }
  .pouch__product-photo span {
    position: absolute; left: 65px; top: 8px; width: 150px; height: 80px;
    border-radius: 40%;
    background: radial-gradient(ellipse at center, #8a9a4a 0%, #a7a65a 55%, rgba(250,211,211,0) 75%);
  }
  .pouch__strain {
    position: absolute; left: 0; width: 100%;
    text-align: center;
  }
  .pouch__strain-name {
    display: inline-block;
    font-size: 15px; letter-spacing: 1px;
    color: var(--ink-soft);
    padding: 0 4px 2px;
    border-bottom: 1px solid var(--green);
  }
  .pouch--back .pouch__strain-name { font-size: 18px; }
  .pouch__strain-meta {
    font-size: 9px; letter-spacing: 1px; margin-top: 5px; color: var(--ink);
  }
  .pouch__url {
    position: absolute; left: 0; width: 100%; top: 460px;
    text-align: center; font-size: 8px; color: var(--ink);
  }
  .pouch__wordmark {
    position: absolute; left: 0; width: 100%; top: 262px;
    text-align: center;
    font-weight: 500; font-size: 40px; letter-spacing: 3px;
    text-transform: uppercase; color: var(--ink);
  }
</style>
</head>
<body>
  <div class="brand-wordmark">Bram's Organic<span class="dot"></span></div>

  <section class="pouch pouch--front">
    <div class="pouch__seal"></div>
    <div class="pouch__band">
      <div class="pouch__band-stripes"></div>
      <svg class="pouch__cross" width="56" height="56" viewBox="0 0 56 56"><path d="M19 0h18v19h19v18H37v19H19V37H0V19h19z" fill="#fff"/></svg>
    </div>
    <p class="pouch__warning"><strong>Contains Medical Cannabis</strong>Keep out of reach of children and pets</p>
    <div class="pouch__product-photo" role="img" aria-label="Photo of a dried cannabis bud"><span></span></div>
    <div class="pouch__strain" style="top:405px">
      <div class="pouch__strain-name">Mango Drift</div>
      <div class="pouch__strain-meta">ORGANIC | 1 GRAM</div>
    </div>
    <p class="pouch__url">www.bramsorganic.com</p>
  </section>

  <section class="pouch pouch--back">
    <div class="pouch__seal"></div>
    <div class="pouch__band">
      <div class="pouch__band-stripes"></div>
      <svg class="pouch__cross" width="56" height="56" viewBox="0 0 56 56"><path d="M19 0h18v19h19v18H37v19H19V37H0V19h19z" fill="#fff"/></svg>
    </div>
    <div class="pouch__wordmark">Bram's Organic</div>
    <div class="pouch__strain" style="top:398px">
      <div class="pouch__strain-name">Mango Drift</div>
      <div class="pouch__strain-meta">ORGANIC | 1 GRAM</div>
    </div>
    <p class="pouch__url">www.bramsorganic.com</p>
  </section>
</body>
</html>
```